VelaMira
Professional
Marnie Tolbeck
Owner
Available for Philadelphia, New Jersey , and New York
VelaMiraPhotography@postvale.com
Im looking for an elagant design... Vela Mira means Bright Sail in italian. My co. is after my baby girl (Lila June)
I photograph Newborns, Babies, maternity, Children, Family's, Engagements, Pets
Baby Face Big smile
Baby Blue/color edit
Mom with Child
bridge city shot
b&w pic of child with fence
flowers with ring

```html
<!DOCTYPE html>
<html lang="en">
<head>
<meta charset="utf-8">
<title>VelaMira Photography – Business Card</title>
<link href="https://fonts.googleapis.com/css2?family=Arimo:wght@400;700&display=swap" rel="stylesheet">
<style>
  :root {
    --backdrop: #e4e4e4;
    --card-top: #2b2b2d;
    --card-bottom: #0b0b0c;
    --ink: #ffffff;
    --ink-soft: #c9c9c9;
    --accent: #2fa8e6;
    --accent-deep: #0d5fa8;
  }
  * { margin: 0; padding: 0; box-sizing: border-box; }
  html, body {
    width: 1200px; height: 1075px; overflow: hidden;
    background: var(--backdrop);
    font-family: "Arimo", Arial, sans-serif;
  }
  .card {
    position: absolute; left: 100px; top: 237px;
    width: 1000px; height: 600px;
    border-radius: 40px;
    background: linear-gradient(180deg, var(--card-top) 0%, #161617 55%, var(--card-bottom) 100%);
    overflow: hidden;
    color: var(--ink);
  }
  .web-address {
    position: absolute; right: 40px; top: 34px;
    font-size: 26px; letter-spacing: 0.5px;
  }
  .brand { position: absolute; left: 66px; top: 62px; }
  .brand-name {
    font-size: 84px; font-weight: 400; line-height: 1; color: var(--ink);
    letter-spacing: 1px;
  }
  .brand-tagline {
    margin: 8px 0 0 214px;
    font-size: 24px; letter-spacing: 4px; color: var(--ink-soft);
  }
  .accent-bar {
    position: absolute; top: 218px; width: 36px; height: 175px;
    background: linear-gradient(90deg, var(--accent-deep), var(--accent) 60%, #8fd6ff);
  }
  .accent-bar.left { left: 0; }
  .accent-bar.right { right: 0; transform: scaleX(-1); }
  .gallery {
    position: absolute; left: 68px; top: 226px;
    display: flex; gap: 22px;
  }
  .photo { width: 267px; height: 166px; }
  .photo.smile { background: linear-gradient(135deg, #e9c3a8, #b8876a 60%, #5b4a42); }
  .photo.mono { background: linear-gradient(135deg, #d6d6d6, #8a8a8a 55%, #3e3e3e); }
  .photo.flowers { background: linear-gradient(135deg, #c9a58f, #d9b7c6 50%, #9a7f86); }
  .owner { position: absolute; left: 68px; top: 432px; }
  .owner-name { font-size: 29px; font-weight: 700; }
  .owner-role { font-size: 26px; color: var(--ink-soft); margin-top: 6px; }
  .contact {
    position: absolute; left: 385px; top: 426px; right: 30px;
    font-size: 25px; line-height: 38px; list-style: none;
    white-space: nowrap;
  }
</style>
</head>
<body>
  <section class="card" aria-label="VelaMira Photography business card">
    <div class="web-address">www.velamira.net</div>

    <div class="brand">
      <div class="brand-name">VelaMira</div>
      <div class="brand-tagline">Photography</div>
    </div>

    <div class="accent-bar left"></div>
    <div class="accent-bar right"></div>

    <div class="gallery">
      <div class="photo smile" role="img" aria-label="Portrait photo of a smiling baby"></div>
      <div class="photo mono" role="img" aria-label="Black and white photo of a young child"></div>
      <div class="photo flowers" role="img" aria-label="Photo of a baby girl among pink flowers"></div>
    </div>

    <div class="owner">
      <div class="owner-name">Marnie Tolbeck</div>
      <div class="owner-role">Owner</div>
    </div>

    <ul class="contact">
      <li>Philadelphia, New Jersey, and New York.</li>
      <li>Phone: 215-555-0147.</li>
      <li>Cell: 215-555-0182.</li>
      <li>Email: VelaMiraPhotography@postvale.com</li>
    </ul>
  </section>
</body>
</html>
```